Give my personal webpage more appeal!

I need my CV website improved - drmeganholt.com.au.
I am using the template KESTREL from pagecraftly. i would like to keep the already existing theme but am open to suggestions.
Please focus on imagery, colour scheme, and textures to enhance the appeal and look of the page.
The content is there, but now I need a designer to improve the look of my page.
I need styling, royalty-free unique modern images to make the page professional, personal and friendly.
I work in healthcare, so I'm a people person.
I teach professionals and I treat a lot of families.

Target Market(s)

Parents, Professional Healthcare providers

Number of Pages Required

1 page

Font styles to use
Serif
Sans Serif

Requirements
Must have
• My face - image at the top, all the information already contained in it.
• Links to the websites I manage such as my blog.
• One Page website.
• All the information it already contains with the ability to have more.
• Ideally, we would keep the same format for the page although I'm happy to expand column and change the page's structure with in the theme template KESTREL.
Nice to have
• The current KESTREL template. I would like to keep the already existing theme but am open to suggestions.
Should not have
• Multiple pages.

```html
<!DOCTYPE html>
<html lang="en">
<head>
<meta charset="utf-8">
<title>Dr Megan Holt — Education</title>
<link href="https://fonts.googleapis.com/css2?family=Montserrat:wght@300;400;700&family=Merriweather:wght@400&display=swap" rel="stylesheet">
<style>
  :root {
    --coral: #ef4b5c;
    --white: #ffffff;
    --ink: #111111;
    --mist: #f5f5f6;
    --card-shadow: rgba(0,0,0,0.22);
    --rule: rgba(255,255,255,0.75);
  }
  * { margin: 0; padding: 0; box-sizing: border-box; }
  html, body { width: 1200px; height: 1000px; overflow: hidden; }
  body {
    position: relative;
    background: var(--white);
    font-family: "Montserrat", Arial, sans-serif;
    color: var(--white);
  }
  .news-card {
    position: absolute;
    background: var(--white);
    box-shadow: 0 1px 3px var(--card-shadow);
  }
  .news-card--left { left: 349px; top: -40px; width: 274px; height: 55px; }
  .news-card--right { left: 667px; top: -40px; width: 274px; height: 98px; }
  .news-card__text {
    position: absolute; left: 19px; top: 33px;
    font-family: "Merriweather", Georgia, serif;
    font-size: 9px; color: #333;
  }
  .education {
    position: absolute; left: 161px; top: 122px;
    width: 1039px; height: 758px;
    background: var(--coral);
  }
  .education__icon { position: absolute; left: 440px; top: 75px; }
  .education__intro {
    position: absolute; left: 89px; top: 211px; width: 860px;
    text-align: center; font-weight: 300; font-size: 19px;
    line-height: 30px; letter-spacing: 0.35px;
  }
  .education__rule {
    position: absolute; left: 151px; top: 347px;
    width: 724px; height: 1px; background: var(--rule);
  }
  .study { position: absolute; }
  .study__num {
    position: absolute; left: 0; top: 0;
    width: 56px; height: 56px; border: 2px solid var(--white);
    border-radius: 50%; display: flex; align-items: center; justify-content: center;
    font-weight: 300; font-size: 19px;
  }
  .study__body {
    position: absolute; width: 240px;
    font-size: 11.5px; line-height: 15px; font-weight: 400; letter-spacing: 0.2px;
  }
  .study__body p + p { margin-top: 15px; }
  .employment {
    position: absolute; left: 161px; top: 880px;
    width: 1039px; height: 120px; background: var(--mist);
  }
  .employment__title {
    position: absolute; left: 162px; top: 77px;
    font-weight: 700; font-size: 17px; color: var(--ink); letter-spacing: 0.3px;
  }
  .employment__title::before {
    content: ""; position: absolute; left: -18px; top: 10px;
    width: 7px; height: 2px; background: var(--coral);
  }
</style>
</head>
<body>
  <div class="news-card news-card--left"></div>
  <div class="news-card news-card--right"><p class="news-card__text">in Adelaide in April.</p></div>

  <section class="education">
    <svg class="education__icon" width="112" height="112" viewBox="0 0 112 112" aria-hidden="true">
      <g fill="none" stroke="#fff" stroke-width="2" stroke-linejoin="round">
        <circle cx="55" cy="54" r="54"/>
        <rect x="27" y="21" width="36" height="42" rx="3"/>
        <rect x="33" y="27" width="17" height="5" rx="2.5"/>
        <path d="M27 56 h36"/>
        <rect x="49" y="39" width="35" height="40" rx="3" fill="#ef4b5c"/>
        <rect x="55" y="45" width="17" height="5" rx="2.5"/>
        <path d="M49 72 h35 M52 75.5 h32"/>
      </g>
    </svg>
    <p class="education__intro">Life is for learning. And the more I learn, the more curious I become.&nbsp; I have a thirst to understand things and am passionately inquisitive.&nbsp; My patients and my children are my greatest teachers.&nbsp; But here are my formal foundation studies.</p>
    <div class="education__rule"></div>

    <div class="study" style="left:176px;top:384px;">
      <div class="study__num">1</div>
      <div class="study__body" style="left:72px;top:13px;">
        <p>Meridian College of Applied<br>Movement</p>
        <p>Diplomate of the International Board of<br>Applied Movement</p>
        <p>Board of Certified Teachers<br>ANTWERP, BELGIUM 2008</p>
      </div>
    </div>
    <div class="study" style="left:539px;top:384px;">
      <div class="study__num">2</div>
      <div class="study__body" style="left:69px;top:4px;">
        <p>Harbourview University</p>
        <p>Master of Chiropractic<br>SYDNEY, AUSTRALIA 2000-2002</p>
      </div>
    </div>
    <div class="study" style="left:176px;top:568px;">
      <div class="study__num">3</div>
      <div class="study__body" style="left:72px;top:13px;">
        <p>Northgate University</p>
        <p>Bachelor of Science (Anatomy)<br>BRISBANE, AUSTRALIA 1997-1999</p>
      </div>
    </div>
    <div class="study" style="left:539px;top:568px;">
      <div class="study__num">4</div>
      <div class="study__body" style="left:69px;top:4px;">
        <p>Harbourview University</p>
        <p>Master of Chiropractic<br>SYDNEY, AUSTRALIA 2000-2002</p>
      </div>
    </div>
  </section>

  <section class="employment">
    <h2 class="employment__title">EMPLOYMENT</h2>
  </section>
</body>
</html>
```